Brilliant Design Needed For Stand Up Pouch - Drink Mix

We need a layout for our resealable stand-up pouch that holds our powered sports drink mix. Target audience is endurance athletes that enjoy marathon running, cycling, mountain biking, hiking and triathlon. Secondary audience are participants in team sports such soccer, lacrosse, football and basketball. Please review the attached project brief for full details. Thanks!

Target Market(s)

50/50 male/female, ages 20-50, USA, succesful, driven, educated. Active, healthy, athletic, outdoor lifestyle.

Industry/Entity Type

Fitness

Font styles to use
Sans Serif

Colors
33a6d7
3277b5
abd037

Requirements
Must have
• Please review the attached project brief for full details.
Nice to have
Should not have

```html
<!DOCTYPE html>
<html lang="en">
<head>
<meta charset="utf-8">
<title>Stridewell Sport Formula – Hydration Drink Mix Pouch</title>
<link rel="stylesheet" href="https://fonts.googleapis.com/css2?family=Exo+2:ital,wght@0,700;0,800;1,700;1,900&family=Roboto:wght@400;500&display=swap">
<style>
  :root {
    --brand-blue: #3277b5;
    --sky-blue: #33a6d7;
    --lime: #abd037;
    --title-blue: #1f6aad;
    --leaf-dark: #4f8a22;
    --leaf-mid: #6ea82c;
    --silver-light: #f2f3f4;
    --silver-mid: #c9cdd1;
    --band-dark: #3d4247;
    --white: #ffffff;
    --gold: #e2b21c;
    --lemon: #f3e04a;
    --shadow-ink: #202326;
  }
  * { box-sizing: border-box; margin: 0; padding: 0; }
  html, body { width: 928px; height: 1200px; overflow: hidden; background: #ececec; }

  .pouch-face {
    position: relative;
    width: 928px;
    height: 1200px;
    overflow: hidden;
    font-family: "Roboto", Arial, sans-serif;
    background: var(--white);
  }

  /* ---------- brand area ---------- */
  .brand {
    position: absolute;
    top: 0; left: 0; right: 0;
    height: 430px;
    background: linear-gradient(180deg, #fafafa 0%, var(--white) 60%, #f4f5f6 100%);
    display: flex;
    align-items: center;
    justify-content: center;
    padding-top: 120px;
  }
  .brand-name {
    display: flex;
    align-items: center;
    gap: 22px;
    font-family: "Exo 2", Arial, sans-serif;
    font-weight: 800;
    font-size: 86px;
    letter-spacing: 2px;
    color: var(--brand-blue);
  }
  .brand-square { width: 58px; height: 58px; background: var(--sky-blue); }

  /* ---------- title band ---------- */
  .title-band {
    position: absolute;
    top: 430px; left: 0; right: 0;
    height: 150px;
    background: linear-gradient(180deg, var(--silver-light) 0%, var(--silver-mid) 55%, #eef0f1 100%);
  }
  .tagline {
    height: 38px;
    background: linear-gradient(90deg, var(--band-dark), #6b7177 60%, var(--band-dark));
    color: var(--white);
    font-family: "Exo 2", Arial, sans-serif;
    font-style: italic;
    font-weight: 700;
    font-size: 24px;
    letter-spacing: 1px;
    text-transform: uppercase;
    line-height: 38px;
    padding-left: 70px;
  }
  .product-title {
    font-family: "Exo 2", Arial, sans-serif;
    font-style: italic;
    font-weight: 900;
    font-size: 96px;
    line-height: 108px;
    letter-spacing: 2px;
    color: var(--title-blue);
    text-transform: uppercase;
    text-align: center;
  }

  /* ---------- green field ---------- */
  .flavour-field {
    position: absolute;
    top: 580px; left: 0; right: 0; bottom: 0;
    background: linear-gradient(160deg, var(--leaf-mid) 0%, var(--leaf-dark) 55%, #3f7a1a 100%);
  }
  .mix-label {
    position: absolute;
    top: 36px; left: 110px;
    font-family: "Exo 2", Arial, sans-serif;
    font-style: italic;
    font-weight: 900;
    color: var(--silver-light);
    line-height: 1;
  }
  .mix-label .line-1 { font-size: 54px; letter-spacing: 2px; text-transform: uppercase; display: block; }
  .mix-label .line-2 { font-size: 46px; display: block; margin-top: 4px; }

  .award-badge {
    position: absolute;
    top: 180px; left: 200px;
    width: 104px; height: 104px;
    border-radius: 50%;
    background: var(--gold);
  }

  .runner-art {
    position: absolute;
    top: 120px; left: 340px;
    width: 240px; height: 360px;
    border-radius: 40px;
    background: linear-gradient(180deg, #2b2f33 0%, var(--shadow-ink) 100%);
    opacity: 0.85;
  }

  .citrus-art {
    position: absolute;
    bottom: 40px; left: 40px;
    width: 180px; height: 110px;
    border-radius: 24px;
    background: linear-gradient(120deg, var(--lemon) 0%, var(--lime) 100%);
  }

  .feature-list {
    position: absolute;
    top: 40px; left: 606px;
    width: 300px;
    list-style: none;
  }
  .feature {
    display: flex;
    align-items: center;
    gap: 16px;
    margin-bottom: 24px;
    color: var(--white);
    font-size: 21px;
    line-height: 1.2;
  }
  .feature-icon { flex: 0 0 66px; width: 66px; height: 66px; }

  .net-weight {
    position: absolute;
    top: 390px; right: 50px;
    display: flex;
    align-items: center;
    color: var(--white);
    font-size: 22px;
    font-weight: 500;
    line-height: 1.3;
  }
  .net-weight .unit-label { padding-right: 14px; border-right: 2px solid var(--white); text-align: right; }
  .net-weight .amount { padding-left: 14px; }

  .flavour-note {
    position: absolute;
    bottom: 40px; left: 440px;
    font-family: "Exo 2", Arial, sans-serif;
    font-style: italic;
    font-weight: 700;
    font-size: 28px;
    line-height: 1.15;
    color: var(--lemon);
  }
</style>
</head>
<body>
<main class="pouch-face">

  <header class="brand">
    <div class="brand-name"><span class="brand-square"></span>STRIDEWELL</div>
  </header>

  <section class="title-band">
    <p class="tagline">Hydration by duration</p>
    <h1 class="product-title">Sport Formula</h1>
  </section>

  <section class="flavour-field">
    <h2 class="mix-label"><span class="line-1">Hydration</span><span class="line-2">Drink Mix</span></h2>

    <div class="award-badge" aria-hidden="true"></div>

    <div class="runner-art" role="img" aria-label="Silhouette of a runner in full stride"></div>

    <ul class="feature-list">
      <li class="feature">
        <svg class="feature-icon" viewBox="0 0 70 70" aria-hidden="true">
          <circle cx="35" cy="35" r="32" fill="#e3e6e8" stroke="#9aa1a6" stroke-width="3"/>
          <rect x="18" y="27" width="30" height="16" rx="2" fill="none" stroke="#333" stroke-width="3"/>
          <rect x="48" y="31" width="4" height="8" fill="#333"/>
          <rect x="21" y="30" width="16" height="10" fill="var(--sky-blue)"/>
        </svg>
        <span>Advanced<br>Hydration System</span>
      </li>
      <li class="feature">
        <svg class="feature-icon" viewBox="0 0 70 70" aria-hidden="true">
          <circle cx="35" cy="35" r="32" fill="#e3e6e8" stroke="#9aa1a6" stroke-width="3"/>
          <path d="M24 18 H46 L43 54 H27 Z" fill="none" stroke="#333" stroke-width="3" stroke-linejoin="round"/>
          <path d="M26 32 H44 L43 52 H27 Z" fill="var(--sky-blue)"/>
        </svg>
        <span>Makes 27, 12 fl oz<br>Servings</span>
      </li>
      <li class="feature">
        <svg class="feature-icon" viewBox="0 0 70 70" aria-hidden="true">
          <circle cx="35" cy="35" r="32" fill="#e3e6e8" stroke="#9aa1a6" stroke-width="3"/>
          <rect x="16" y="24" width="8" height="22" rx="2" fill="#333"/>
          <rect x="46" y="24" width="8" height="22" rx="2" fill="#333"/>
          <rect x="24" y="32" width="22" height="6" fill="#333"/>
        </svg>
        <span>Recommended For<br>Workouts<br>Lasting 1 Hour</span>
      </li>
    </ul>

    <div class="net-weight">
      <span class="unit-label">NET<br>WT.</span>
      <span class="amount">15.5 OZ<br>(440G)</span>
    </div>

    <div class="citrus-art" role="img" aria-label="Lemon and lime slices"></div>
    <p class="flavour-note">Lemon-Lime with<br>other natural flavors</p>
  </section>

</main>
</body>
</html>
```